依頼詳細
不動産物件情報の冊子の表紙デザインです。5月らしいイメージと、簡単には捨てられないインパクトのあるデザインをお願いします。
会社WEB:http://morinaga-hoshizora.jp/
記載項目
タイトル「物件情報 2019 5月号」 会社ロゴ:添付参照
希望イメージ
シンプル 複雑
単色 カラフル
暗い 明るい
日常 高級
遊び心 厳粛
未来的 伝統的
女性的 男性的
希望する色
納品ファイル
• イラストレーター形式 (.ai)
補足説明
四半期に一度発行予定ですので、継続の可能性もあります
参考までに新春号のデータを添付いたします
先述の、物件情報は、関東・九州の情報が主ですが、全国の情報を掲載しております。
■ 選んだ理由

弊社の意図をよくご理解いただき、季節に合ったご提案をいただきました。データ化の対応も迅速な対応で、助かりました。引き続きよろしくお願いします

■ 提案者全員のお礼・コメント

たくさんのご提案をいただき、参加いただいた皆様には深謝いたします。
どのご提案も、素晴らしいものでした。

次号は夏ごろを予定しておりますので、その折には、また多くの方々のご提案をいただくことができればと存じます。
今後ともよろしくお願いいたします

```html
<!DOCTYPE html>
<html lang="ja">
<head>
<meta charset="utf-8">
<title>物件情報 2019 5月号</title>
<link rel="stylesheet" href="https://fonts.googleapis.com/css2?family=Noto+Sans+JP:wght@900&family=Noto+Serif+JP:wght@700;900&display=swap">
<style>
  :root {
    --paper: #ffffff;
    --trim: #9a9a9a;
    --sky-top: #3a86c8;
    --sky-mid: #9fd0ee;
    --sky-light: #e6f2fa;
    --sea: #6aa7cf;
    --city: #aebfcb;
    --streamer-navy: rgba(22, 58, 120, .85);
    --streamer-black: rgba(20, 28, 48, .8);
    --streamer-red: rgba(205, 40, 52, .7);
    --streamer-pink: rgba(236, 120, 130, .5);
    --streamer-green: rgba(70, 150, 90, .45);
    --title-green: #3fb93a;
    --ink-dark: #17324a;
    --white: #ffffff;
    --brand-gold: #e0a21f;
  }
  * { margin: 0; padding: 0; box-sizing: border-box; }
  html, body { width: 875px; height: 1200px; overflow: hidden; background: var(--paper); }
  .cover-sheet { position: relative; width: 875px; height: 1200px; }
  .trim-marks { position: absolute; inset: 0; }
  .cover {
    position: absolute; left: 40px; top: 36px; width: 795px; height: 1128px; overflow: hidden;
  }
  .cover-photo {
    position: absolute; inset: 0;
    background:
      linear-gradient(58deg,
        rgba(0,0,0,0) 34%,
        var(--streamer-green) 40%,
        var(--streamer-navy) 47%,
        var(--streamer-black) 55%,
        var(--streamer-red) 64%,
        var(--streamer-pink) 71%,
        rgba(0,0,0,0) 79%),
      linear-gradient(180deg,
        rgba(0,0,0,0) 0%, rgba(0,0,0,0) 84%,
        rgba(150,165,180,.6) 92%, rgba(120,140,155,.7) 100%),
      linear-gradient(180deg, var(--sky-top) 0%, var(--sky-mid) 30%, var(--sky-light) 62%, var(--sea) 78%, var(--city) 100%);
  }
  .title-main {
    position: absolute; left: 40px; top: 48px; width: 715px;
    font-family: "Noto Sans JP", sans-serif; font-weight: 900;
    font-size: 172px; line-height: 1; letter-spacing: 4px; text-align: center;
    color: var(--title-green);
    -webkit-text-stroke: 8px var(--white); paint-order: stroke fill;
    text-shadow: 0 0 3px var(--ink-dark), 0 4px 8px rgba(0,0,0,.45);
  }
  .title-year {
    position: absolute; left: 44px; top: 240px;
    font-family: "Noto Sans JP", sans-serif; font-weight: 900;
    font-size: 138px; line-height: 1; letter-spacing: 2px;
    color: var(--white);
    -webkit-text-stroke: 6px var(--ink-dark); paint-order: stroke fill;
    text-shadow: 0 4px 8px rgba(0,0,0,.4);
  }
  .title-issue {
    position: absolute; left: 466px; top: 252px; width: 290px; height: 104px;
    background: var(--white); border: 6px solid var(--ink-dark); border-radius: 6px;
    display: flex; align-items: center; justify-content: center;
    font-family: "Noto Serif JP", serif; font-weight: 900;
    font-size: 78px; line-height: 1; color: var(--ink-dark);
  }
  .tagline {
    position: absolute; left: 168px; top: 600px; height: 400px;
    writing-mode: vertical-rl;
    font-family: "Noto Serif JP", serif; font-weight: 700;
    font-size: 34px; line-height: 1.5; letter-spacing: 5px;
    color: var(--white);
    text-shadow: 0 0 6px rgba(20,50,90,.9), 0 2px 4px rgba(0,0,0,.5);
  }
  .tagline .line-two { display: block; padding-top: 40px; }
  .brand {
    position: absolute; left: 316px; top: 1000px; width: 165px;
    display: flex; flex-direction: column; align-items: center; gap: 6px;
  }
  .brand-dot { width: 42px; height: 42px; border-radius: 50%; background: var(--brand-gold); }
  .brand-name {
    font-family: "Noto Sans JP", sans-serif; font-weight: 900;
    font-size: 22px; line-height: 1.1; text-align: center; color: var(--ink-dark);
  }
</style>
</head>
<body>
<div class="cover-sheet">
  <svg class="trim-marks" width="875" height="1200" viewBox="0 0 875 1200" aria-hidden="true">
    <g stroke="var(--trim)" stroke-width="1" fill="none">
      <path d="M0 36H30M40 0V26M0 24H18M28 0V14"/>
      <path d="M875 36H845M835 0V26M875 24H857M847 0V14"/>
      <path d="M0 1164H30M40 1200V1174M0 1176H18M28 1200V1186"/>
      <path d="M875 1164H845M835 1200V1174M875 1176H857M847 1200V1186"/>
      <path d="M437 0V20M0 600H20M875 600H855M437 1200V1180"/>
    </g>
  </svg>

  <main class="cover">
    <div class="cover-photo" role="img" aria-label="五月の青空に斜めに連なってはためく青・黒・赤の鯉のぼりと、その下に広がる海辺の街並みとタワーの風景写真"></div>

    <h1 class="title-main">物件情報</h1>
    <p class="title-year">2019</p>
    <p class="title-issue">5月号</p>

    <p class="tagline">不動産で九州・東京・<span class="line-two">アジアを繋げる。</span></p>

    <div class="brand">
      <span class="brand-dot"></span>
      <span class="brand-name">Hoshizora<br>Corporation</span>
    </div>
  </main>
</div>
</body>
</html>
```